Landing page design for a tech event

A landing page for my event for marketing & business professionals to learn the latest digital contents driven marketing by Quorvel an open source CMS. We need a full web design and code for this responsive landing page.

I would like to have a simple, big UI, flat design and fast loading design with minimum set of color (like B&W + One) but with very audacious creative concept to get people's attention and let them focus on contents.

Target Market(s)

Marketing managers in mid-large enterprises.

Industry/Entity Type

Information Technology

Coding

Coded - Design and coding required

Number of Pages Required

1 page

Font styles to use
Sans Serif

Colors
333333
5c5c5c
9d9d9d
d9d9d9
eeeeee
9bcb3b
add136
cadf82
eaf2ce

Requirements
Must have
• 1. A responsive landing page to promote a tech event with ridiculously good looking creative.
• 2. The landing page must have PC and Smart Phones design as responsive web.
• 3. The landing page must have header menu, top section, about section, program & speakers section, tickets information section, sponsors section, contact section and venue (address & map) section and footer.
• 4. The landing page must have our logo (attached)
• 5. For ticket information section, we will add a widget (attached) from Lantomi.com for ticket sales.
• 6. My request is for you to design an English page but we will use exact same design for Japanese contents as well. so at the end of day, there will be two pages and we need a button to switch page (language) in the header menu.
• 7. Full set of code HTML/CSS/JS.
Nice to have
• Inspirational websites are here.
• For creative:
• http://ateliervortane.com/
• http://www.cruzelmdale.com/
• http://www.plonkit.com/band/
• For contents
• http://meets.dravonhub.com/kx2015/
• http://www.weavebuildpacifica.com
Should not have
• More than one page! ;-)

```html
<!DOCTYPE html>
<html lang="en">
<head>
<meta charset="utf-8">
<title>Norvanta Event</title>
<link href="https://fonts.googleapis.com/css2?family=Open+Sans:ital,wght@0,300;0,400;0,600;0,700;1,400;1,600&display=swap" rel="stylesheet">
<style>
:root{
  --ink:#333333;
  --ink-soft:#5c5c5c;
  --mute:#9d9d9d;
  --line:#d9d9d9;
  --paper:#eeeeee;
  --paper-light:#f5f5f5;
  --white:#ffffff;
  --brand:#d42a3c;
  --accent:#e3b23c;
  --green:#4caf50;
}
*{margin:0;padding:0;box-sizing:border-box}
html,body{width:1200px;height:2970px;overflow:hidden}
body{font-family:"Open Sans",Arial,sans-serif;color:var(--ink);background:var(--white);position:relative}
.abs{position:absolute}
/* top nav */
.topnav{left:0;top:0;width:1200px;height:54px;background:#666;display:flex;align-items:center;justify-content:space-between;padding:0 100px}
.topnav a{color:var(--white);font-size:12px;text-decoration:none;letter-spacing:.3px}
.topnav svg{width:18px;height:18px}
/* header */
.header{left:0;top:54px;width:1200px;height:96px;background:var(--white)}
.brand{left:100px;top:26px;display:flex;align-items:center;gap:10px;font-weight:700;font-size:34px;color:var(--brand);letter-spacing:-1px}
.brand i{display:block;width:14px;height:14px;background:var(--brand);border-radius:50%}
.lang{left:1004px;top:32px;width:96px;height:34px;background:var(--ink-soft);color:var(--white);font-size:11px;display:flex;align-items:center;padding-left:8px}
.lang span.sep{position:absolute;right:26px;top:4px;width:1px;height:26px;background:#888}
.lang svg{position:absolute;right:8px;top:13px}
/* hero */
.hero{left:0;top:150px;width:1200px;height:634px;background:linear-gradient(100deg,#9aa7b0 0%,#c9d0d4 35%,#b6bcbe 55%,#3d4452 80%,#6b6660 100%)}
.hero-title{left:0;top:356px;width:1200px;text-align:center;color:var(--white);font-weight:700;font-size:52px;line-height:60px}
.hero-sub{left:0;top:452px;width:1200px;text-align:center;color:var(--white);font-size:21px;line-height:38px}
.hero-strip{left:0;top:762px;width:1200px;height:22px;background:rgba(60,60,60,.75)}
.dots{left:535px;top:740px;width:130px;height:34px;background:rgba(60,60,60,.9);display:flex;justify-content:center;align-items:center;gap:10px}
.dots b{width:12px;height:12px;border-radius:50%;background:var(--white)}
.dots b.on{background:#222;border:2px solid #fff}
/* section titles */
.sec-title{left:0;width:1200px;text-align:center;font-weight:300;font-size:41px;color:#555}
/* about */
.about{left:0;top:784px;width:1200px;height:282px;background:var(--white)}
.about p{position:absolute;left:160px;top:130px;width:880px;text-align:center;font-size:11px;font-style:italic;line-height:30px;color:#666}
/* program */
.program{left:0;top:1066px;width:1200px;height:634px;background:var(--paper-light)}
.speaker{position:absolute;width:500px;height:160px}
.speaker .photo{position:absolute;left:0;top:0;width:158px;height:158px;border-radius:50%;border:4px solid var(--white)}
.speaker h3{position:absolute;left:183px;top:12px;font-style:italic;font-weight:600;font-size:21px;color:var(--ink)}
.speaker h4{position:absolute;left:183px;top:52px;font-weight:600;font-size:15px;color:#444;white-space:nowrap}
.speaker p{position:absolute;left:183px;top:80px;width:300px;font-size:12px;line-height:26px;color:#666}
/* tickets */
.tickets{left:0;top:1700px;width:1200px;height:518px;background:#f2f2f2}
.widget{left:311px;top:150px;width:576px;height:302px;background:var(--line)}
.widget-name{position:absolute;left:0;top:18px;width:576px;display:flex;justify-content:center;align-items:center;gap:10px;font-weight:600;font-size:38px;color:#444}
.widget-name i{display:block;width:26px;height:26px;border-radius:50%;background:var(--green)}
.field{position:absolute;background:var(--paper);font-size:11px;color:#555;display:flex;align-items:center;padding-left:18px;height:41px}
.btn-book{position:absolute;left:188px;top:225px;width:190px;height:50px;background:#2b2b2b;color:#fff;font-weight:600;font-size:17px;letter-spacing:1px;display:flex;align-items:center;justify-content:center}
/* sponsors */
.sponsors{left:0;top:2218px;width:1200px;height:238px;background:#f7f7f7}
.badge{position:absolute;top:65px;width:132px;height:106px;background:var(--white);display:flex;flex-direction:column;align-items:center;justify-content:center;gap:10px}
.badge i{display:block;width:52px;height:52px;border-radius:50%;background:var(--mute)}
.badge u{display:block;width:70px;height:8px;background:var(--line)}
/* contact */
.map{left:0;top:2456px;width:1200px;height:296px;background:linear-gradient(120deg,#e6e3d8 0%,#dcdfd4 40%,#e8e6dc 70%,#d6dccf 100%)}
.contact{left:424px;top:2471px;width:352px;height:266px;background:rgba(70,70,70,.88);color:#fff}
.contact h2{position:absolute;left:0;top:28px;width:352px;text-align:center;font-weight:600;font-size:25px;letter-spacing:.5px}
.row{position:absolute;left:70px;display:flex;align-items:center;gap:22px;font-size:13px}
.row svg{width:18px;height:18px}
.btn-map{position:absolute;left:87px;top:208px;width:186px;height:42px;border:2px solid var(--accent);display:flex;align-items:center;justify-content:center;font-size:12px;font-weight:600}
/* footer */
.footer{left:0;top:2752px;width:1200px;height:218px;background:var(--ink);color:#fff}
.social{position:absolute;top:36px;width:56px;height:56px;border:2px solid #fff;border-radius:50%;display:flex;align-items:center;justify-content:center;font-size:15px;font-weight:600;color:#fff}
.foot-links{position:absolute;left:0;top:126px;width:1200px;display:flex;justify-content:center;gap:14px;font-size:12px}
.foot-links span.sep{color:#777}
.copy{position:absolute;left:0;top:162px;width:1200px;text-align:center;font-size:11px;color:#ddd}
</style>
</head>
<body>

<nav class="abs topnav">
  <a>HOME</a><a>ABOUT</a><a>PROGRAM</a><a>TICKETS</a><a>SPONSORS</a><a>CONTACT US</a>
  <svg viewBox="0 0 20 20"><circle cx="8" cy="8" r="6" fill="none" stroke="#fff" stroke-width="2.4"/><line x1="12.5" y1="12.5" x2="18" y2="18" stroke="#fff" stroke-width="2.8"/></svg>
</nav>

<header class="abs header">
  <div class="abs brand"><i></i>Norvanta</div>
  <div class="abs lang">ENGLISH<span class="sep"></span>
    <svg width="10" height="7" viewBox="0 0 10 7"><path d="M0 0h10L5 7z" fill="#fff"/></svg>
  </div>
</header>

<section class="abs hero" role="img" aria-label="Photo of business people talking around a meeting table"></section>
<div class="abs hero-title">Norvanta</div>
<div class="abs hero-sub">Neque porro quisquam est qui dolorem<br>ipsum quia dolor sit amet .</div>
<div class="abs hero-strip"></div>
<div class="abs dots"><b class="on"></b><b></b><b></b><b></b></div>

<section class="abs about">
  <h2 class="abs sec-title" style="top:56px">About Us</h2>
  <p>Sed ut perspiciatis unde omnis iste natus error sit voluptatem accusantium doloremque laudantium, totam rem aperiam, eaque ipsa quae ab illo inventore veritatis et quasi architecto beatae vitae dicta sunt explicabo. Nemo enim ipsam voluptatem quia voluptas sit aspernatur aut odit aut fugit, sed quia consequuntur magni dolores eos qui ratione voluptatem sequi nesciunt.</p>
</section>

<section class="abs program">
  <h2 class="abs sec-title" style="top:52px">Program &amp; Speakers</h2>
  <div class="speaker" style="left:100px;top:182px">
    <div class="photo" role="img" aria-label="Portrait photo of speaker Clara" style="background:radial-gradient(circle at 50% 38%,#c9a58a 0 18%,transparent 19%),linear-gradient(180deg,#eef1f3 0%,#eef1f3 55%,#8fb0d0 56%,#7ea2c8 100%)"></div>
    <h3>Clara</h3><h4>MOLESTIAS EXCEPTURI OCCAECATI CUPI</h4>
    <p>At vero eos et accusamus et iusto odio dignissimos ducimus qui blanditiis praesentium voluptatum deleniti atque corrupti quos .</p>
  </div>
  <div class="speaker" style="left:624px;top:182px">
    <div class="photo" role="img" aria-label="Portrait photo of speaker John" style="background:radial-gradient(circle at 50% 36%,#d8b39a 0 17%,transparent 18%),linear-gradient(180deg,#f0f0f0 0%,#f0f0f0 55%,#2f3440 56%,#262a33 100%)"></div>
    <h3>John</h3><h4>MOLESTIAS EXCEPTURI OCCAECATI CUPI</h4>
    <p>At vero eos et accusamus et iusto odio dignissimos ducimus qui blanditiis praesentium voluptatum deleniti atque corrupti quos .</p>
  </div>
  <div class="speaker" style="left:100px;top:406px">
    <div class="photo" role="img" aria-label="Portrait photo of speaker Mark" style="background:radial-gradient(circle at 50% 34%,#c99f84 0 17%,transparent 18%),linear-gradient(180deg,#f4f4f4 0%,#f4f4f4 55%,#283040 56%,#1f2530 100%)"></div>
    <h3>Mark</h3><h4>MOLESTIAS EXCEPTURI OCCAECATI CUPI</h4>
    <p>At vero eos et accusamus et iusto odio dignissimos ducimus qui blanditiis praesentium voluptatum deleniti atque corrupti quos .</p>
  </div>
  <div class="speaker" style="left:624px;top:406px">
    <div class="photo" role="img" aria-label="Portrait photo of speaker Agnes" style="background:radial-gradient(circle at 50% 38%,#e6c79a 0 20%,transparent 21%),linear-gradient(180deg,#f6f3ee 0%,#f6f3ee 58%,#cfe0ee 59%,#bcd3e6 100%)"></div>
    <h3>Agnes</h3><h4>MOLESTIAS EXCEPTURI OCCAECATI CUPI</h4>
    <p>At vero eos et accusamus et iusto odio dignissimos ducimus qui blanditiis praesentium voluptatum deleniti atque corrupti quos .</p>
  </div>
</section>

<section class="abs tickets">
  <h2 class="abs sec-title" style="top:50px">Ticket Information</h2>
  <div class="abs widget">
    <div class="widget-name"><i></i>Lantomi</div>
    <div class="field" style="left:47px;top:87px;width:484px">EVENT TITLE</div>
    <div class="field" style="left:47px;top:154px;width:230px">DATE
      <svg style="position:absolute;right:10px;top:13px" width="10" height="15" viewBox="0 0 10 15"><path d="M0 6h10L5 0zM0 9h10L5 15z" fill="#333"/></svg>
    </div>
    <div class="field" style="left:299px;top:154px;width:232px">DATE</div>
    <div class="btn-book">BOOK NOW</div>
  </div>
</section>

<section class="abs sponsors">
  <div class="badge" style="left:100px" role="img" aria-label="Sponsor badge"><i style="background:#7fa6c9"></i><u></u></div>
  <div class="badge" style="left:326px" role="img" aria-label="Sponsor badge"><i style="background:#e8a93a"></i><u></u></div>
  <div class="badge" style="left:532px" role="img" aria-label="Sponsor badge"><i style="background:#2e86c8"></i><u></u></div>
  <div class="badge" style="left:760px" role="img" aria-label="Sponsor badge"><i style="background:#3aa3c4"></i><u></u></div>
  <div class="badge" style="left:956px" role="img" aria-label="Sponsor badge"><i style="background:#8cc63f"></i><u></u></div>
</section>

<section class="abs map" role="img" aria-label="Street map of the venue area"></section>
<div class="abs contact">
  <h2>CONTACT US</h2>
  <div class="row" style="top:86px">
    <svg viewBox="0 0 20 20"><path d="M10 1a6 6 0 0 0-6 6c0 5 6 12 6 12s6-7 6-12a6 6 0 0 0-6-6z" fill="#fff"/><circle cx="10" cy="7" r="2.3" fill="#464646"/></svg>
    <span>No; 234 Elm Street Harbury</span></div>
  <div class="row" style="top:122px">
    <svg viewBox="0 0 20 20"><path d="M5 2l3 4-2 2c1 2 3 4 5 5l2-2 4 3-2 4C9 17 3 11 2 4z" fill="#fff"/></svg>
    <span>555-0199-214</span></div>
  <div class="row" style="top:158px">
    <svg viewBox="0 0 20 20"><rect x="1" y="4" width="18" height="13" fill="#fff"/><path d="M1 4l9 7 9-7" fill="none" stroke="#464646" stroke-width="1.6"/></svg>
    <span>NRV@Sample.com</span></div>
  <div class="btn-map">View Location on Map</div>
</div>

<footer class="abs footer">
  <div class="social" style="left:456px" aria-label="Social link Kivo">Kv</div>
  <div class="social" style="left:534px" aria-label="Social link Tazel">Tz</div>
  <div class="social" style="left:610px" aria-label="Social link Gomra">Gm</div>
  <div class="social" style="left:687px" aria-label="Social link Lunet">Ln</div>
  <div class="foot-links"><span>Home</span><span class="sep">|</span><span>About</span><span class="sep">|</span><span>Program</span><span class="sep">|</span><span>Tickets</span><span class="sep">|</span><span>Sponsors</span><span class="sep">|</span><span>Contact Us</span></div>
  <div class="copy">Copyright © 2015 NRV. All rights reserved.</div>
</footer>

</body>
</html>
```